FelixHarlan's Signature Beard Oil Label Design

I'm looking for a creative designer to run with the design. I am not sure what I really want so surprise me. What ever you do please use earth tone colors. The bottles I use is 2.0 ounces. It is a Boston amber bottle with glass dropper. It is 1.5 width by 3.75 inch height. :Benefits : * Organic * Hair growth* Repairs Split Ends* Softens * Health Shine* Aromatherapy fragrance* Reduce Itching/Irritation * Reduce Dandruff* Reduces Flyaway hair Directions: Place a nickel size drop into palm of handMassage into beard 2 to 3 times a day

Target Market(s)

MEN WITH BEARDS AND MEN THAT WANT TO GROW BEARDS BUT DON'T KNOW HOW

Industry/Entity Type

Hair Care Product

Font styles to use
Serif
Script

Colors
1b1b1b
fdf9cf
ffc214
ffffff

Requirements
Must have
• FALL COLOR SCHEME, Felix Harlan written in a fancy cursive script, all others can me different, please use the gold lion logo without the word Lion.
Nice to have
• CLASSY, MANLY, OLD AND NEW SCHOOL ESSENCE
Should not have
• Anything feminine, Pine Hollow

```html
<!DOCTYPE html>
<html lang="en">
<head>
<meta charset="utf-8">
<title>Felix Harlan Beard Oil Labels</title>
<link rel="stylesheet" href="https://fonts.googleapis.com/css2?family=Alfa+Slab+One&family=Bebas+Neue&family=Great+Vibes&family=Hind:wght@600;700&display=swap">
<style>
  :root {
    --navy: #0d1824;
    --navy-shade: #2f3a46;
    --cream: #fffbd2;
    --gold: #c9924a;
    --gold-bright: #dca13a;
    --ink: #16202c;
    --white: #ffffff;
  }
  * { margin: 0; padding: 0; box-sizing: border-box; }
  html, body { width: 1200px; height: 959px; overflow: hidden; }
  body { position: relative; font-family: "Hind", Arial, sans-serif; }

  .label { position: absolute; left: 0; width: 1200px; overflow: hidden; }
  .label--dark { top: 0; height: 480px; background: var(--navy); color: var(--white); }
  .label--light { top: 480px; height: 479px; background: var(--cream); color: var(--ink); }

  .art { position: absolute; }
  .art--side-left { left: 0; top: 0; width: 150px; height: 480px; background: var(--navy-shade); border-radius: 0 70px 40px 0; opacity: .85; }
  .art--side-right { right: 0; top: 0; width: 155px; height: 480px; background: var(--navy-shade); border-radius: 70px 0 0 40px; opacity: .85; }
  .art--portrait { left: 256px; top: 12px; width: 150px; height: 467px; background: var(--gold-bright); border-radius: 60px 0 0 90px; opacity: .9; }
  .art--mini-face { left: 490px; top: 150px; width: 22px; height: 40px; background: var(--gold-bright); border-radius: 8px; }

  .name-band { position: absolute; left: 405px; top: 0; width: 77px; height: 479px; background: var(--gold-bright); }
  .name-band span {
    position: absolute; left: 50%; top: 50%;
    transform: translate(-50%, -50%) rotate(-90deg);
    font-family: "Bebas Neue", Impact, sans-serif; font-size: 66px; letter-spacing: 8px;
    color: var(--ink); white-space: nowrap; line-height: 1;
  }

  .brand { position: absolute; left: 490px; width: 220px; text-align: center; }
  .brand__mark { display: block; width: 16px; height: 16px; margin: 0 auto 2px; border-radius: 50%; background: var(--gold); }
  .brand__name { font-family: "Great Vibes", cursive; font-weight: 400; font-size: 36px; color: var(--gold); line-height: 1.1; white-space: nowrap; }
  .label--dark .brand { top: 68px; }
  .label--light .brand { top: 44px; }

  .title { position: absolute; left: 500px; width: 200px; text-align: center; }
  .title__beard { font-family: "Bebas Neue", Impact, sans-serif; font-size: 82px; line-height: 1; letter-spacing: 1px; }
  .title__divider { display: block; width: 150px; height: 8px; margin: 2px auto 4px; background: var(--gold); border-radius: 4px; }
  .title__oil { font-family: "Alfa Slab One", Georgia, serif; font-size: 42px; line-height: 1; }
  .label--dark .title { top: 150px; color: var(--white); }
  .label--light .title { top: 146px; color: var(--ink); }

  .ribbon { position: absolute; left: 490px; width: 220px; height: 27px; }
  .ribbon svg { position: absolute; inset: 0; }
  .ribbon span { position: relative; display: block; text-align: center; font-weight: 700; font-size: 16px; line-height: 29px; color: var(--ink); }
  .label--dark .ribbon { top: 301px; }
  .label--light .ribbon { top: 292px; }

  .volume { position: absolute; left: 522px; width: 160px; height: 122px; border-radius: 20px 20px 80px 80px; text-align: center; padding-top: 48px; font-weight: 700; font-size: 17px; line-height: 25px; }
  .label--dark .volume { top: 322px; background: rgba(201,146,74,.28); color: var(--white); }
  .label--light .volume { top: 313px; background: rgba(227,179,90,.35); color: var(--ink); }
  .volume p + p { border-top: 2px solid currentColor; width: 60px; margin: 0 auto; }

  .info { position: absolute; width: 260px; text-align: center; font-weight: 600; font-size: 16.5px; line-height: 24.1px; }
  .info ul { list-style: none; }
  .label--dark .info { left: 812px; top: 62px; color: var(--white); }
  .label--light .info { left: 893px; top: 49px; color: var(--ink); }
  .info__directions { margin-top: 18px; }
  .label--light .info__directions { margin-top: 42px; }
</style>
</head>
<body>

<section class="label label--dark">
  <div class="art art--side-left" role="img" aria-label="Stylised bearded man silhouette, left half"></div>
  <div class="art art--side-right" role="img" aria-label="Stylised bearded man silhouette, right half"></div>

  <div class="brand"><span class="brand__mark"></span><p class="brand__name">Felix Harlan</p></div>

  <div class="title">
    <p class="title__beard">BEARD</p>
    <span class="title__divider" role="img" aria-label="Ornamental star divider"></span>
    <p class="title__oil">OIL</p>
  </div>

  <div class="volume" role="img" aria-label="Beard outline illustration framing the volume">
    <p>2 FL OZ</p><p>60 ML</p>
  </div>

  <div class="ribbon">
    <svg viewBox="0 0 220 27" preserveAspectRatio="none"><polygon points="0,0 220,0 210,13.5 220,27 0,27 10,13.5" fill="var(--gold)"/></svg>
    <span>PROFESSIONAL SERVICES</span>
  </div>

  <div class="info">
    <ul>
      <li>Organic</li><li>Hair growth</li><li>Repairs Split Ends</li><li>Softens</li><li>Health Shine</li>
      <li>Aromatherapy</li><li>Reduce Itching/Irritation</li><li>Reduce Dandruff</li><li>Reduces Flyaway hair</li>
    </ul>
    <div class="info__directions">
      <p>Directions:</p><p>Place a nickel size drop into</p><p>palm of hand</p><p>Massage into beard</p><p>2 to 3 times a day</p>
    </div>
  </div>
</section>

<section class="label label--light">
  <div class="art art--portrait" role="img" aria-label="Stylised bearded man half-portrait in gold"></div>
  <div class="name-band"><span>FELIX HARLAN</span></div>

  <div class="brand"><span class="brand__mark"></span><p class="brand__name">Felix Harlan</p></div>

  <div class="art art--mini-face" role="img" aria-label="Small bearded man icon"></div>
  <div class="title">
    <p class="title__beard">BEARD</p>
    <span class="title__divider" role="img" aria-label="Ornamental star divider"></span>
    <p class="title__oil">OIL</p>
  </div>

  <div class="volume" role="img" aria-label="Beard outline illustration framing the volume">
    <p>2 FL OZ</p><p>60 ML</p>
  </div>

  <div class="ribbon">
    <svg viewBox="0 0 220 27" preserveAspectRatio="none"><polygon points="0,0 220,0 210,13.5 220,27 0,27 10,13.5" fill="var(--gold-bright)"/></svg>
    <span>PROFESSIONAL SERVICES</span>
  </div>

  <div class="info">
    <ul>
      <li>Organic</li><li>Hair growth</li><li>Repairs Split Ends</li><li>Softens</li><li>Health Shine</li>
      <li>Aromatherapy</li><li>Reduce Itching/Irritation</li><li>Reduce Dandruff</li><li>Reduces Flyaway hair</li>
    </ul>
    <div class="info__directions">
      <p>Directions:</p><p>Place a nickel size drop into</p><p>palm of hand</p><p>Massage into beard</p><p>2 to 3 times a day</p>
    </div>
  </div>
</section>

</body>
</html>
```